Company Creation Website Redesign

Firmly789 is an Australian company creation website that specialises in creating company and trust documents. Our website was created in 2014 and we would like a new fresh look. We would like to maintain the same colour scheme of light blue and white. We feel the current landing page is a bit busy and would like something cleaner and more minimalist.

We would like all toolbar options to be the same but redesigned with better font, more aesthetically pleasing etc.

The website is built on AngularJS framework with HTML/CSS markup.

Please have a look at the current landing page.
firmly789.com.au

Target Market(s)

Accountants, those want to create company

Industry/Entity Type

Commerce

Coding

Coded - Design and coding required

Number of Pages Required

5+ page

Font styles to use
Sans Serif

Colors
0054AA
0677BA
7BADD7
CADEEF
E8F1F8

Requirements
Must have
• Attractive symbols
Nice to have
• Simple colour scheme
Should not have
• Busy images

```html
<!DOCTYPE html>
<html lang="en">
<head>
<meta charset="utf-8">
<title>Firmly789 — Australian Online Company Registration</title>
<link href="https://fonts.googleapis.com/css2?family=Montserrat:wght@300;400;500;600;700&display=swap" rel="stylesheet">
<style>
:root{
  --deep:#0054AA;
  --mid:#0677BA;
  --soft:#7BADD7;
  --pale:#CADEEF;
  --mist:#E8F1F8;
  --ink:#1b1f2a;
  --grey:#6b7280;
  --white:#ffffff;
  --red:#f25c5c;
  --star:#f06a3b;
}
*{box-sizing:border-box;margin:0;padding:0}
html,body{width:1200px;height:4267px;overflow:hidden}
body{font-family:'Montserrat',sans-serif;color:var(--ink);background:var(--white);position:relative}
section,header,footer,nav{position:relative;width:1200px;overflow:hidden}
.abs{position:absolute}
a{color:inherit;text-decoration:none}

/* top bar */
.topbar{height:24px;background:var(--mist);font-size:7.5px;color:var(--mid)}
.topbar .service{left:44px;top:8px}
.topbar .phone{left:160px;top:8px}
.topbar .login{left:1015px;top:5px;width:48px;height:14px;border-radius:3px;background:var(--pale);color:var(--deep);text-align:center;line-height:14px;font-weight:600}
.topbar .search{left:1075px;top:6px;width:62px;height:12px;border-bottom:1px solid var(--pale);color:#a8b4c4;font-size:6.5px}
.topbar svg{left:1143px;top:6px}

/* nav */
.nav{height:54px;background:linear-gradient(90deg,var(--deep),var(--mid))}
.brand{display:flex;align-items:center;gap:6px;color:var(--white);font-weight:700;font-size:12px;white-space:nowrap}
.brand i{width:10px;height:10px;border-radius:50%;background:var(--white);display:block}
.nav .brand{left:44px;top:20px}
.nav ul{list-style:none;display:flex;gap:12px;left:160px;top:23px;font-size:6.6px;color:var(--white);font-weight:500;white-space:nowrap}

/* hero */
.hero{height:472px;background:linear-gradient(120deg,var(--white) 0%,var(--white) 18%,var(--mist) 18.2%,var(--pale) 100%)}
.hero h1{left:95px;top:95px;font-size:43px;line-height:52px;color:var(--deep);font-weight:400}
.hero h1 b{font-weight:600}
.hero .lead{left:95px;top:220px;font-size:13.5px;display:flex;align-items:center;gap:10px}
.hero .lead span{color:var(--red);font-size:20px;font-weight:500}
.btn{display:inline-block;background:var(--pale);color:var(--deep);font-size:9.5px;font-weight:600;border-radius:4px;padding:8px 18px;letter-spacing:.3px}
.hero .btn1{left:95px;top:266px}
.hero h2{left:95px;top:320px;font-size:22px;line-height:31px;font-weight:500}
.hero .agent{left:95px;top:396px;font-size:8.5px;color:var(--deep);font-weight:600}
.hero .btn2{left:95px;top:434px}
.hero .art{left:450px;top:20px;width:640px;height:410px;border-radius:40% 30% 10% 30%;background:radial-gradient(circle at 45% 55%,#f7c948 0,#f7c948 9%,transparent 9.5%),radial-gradient(circle at 65% 45%,#3ed1c2 0,#3ed1c2 8%,transparent 8.5%),radial-gradient(circle at 78% 55%,#ef5b5b 0,#ef5b5b 8%,transparent 8.5%),linear-gradient(160deg,var(--mist),var(--pale))}
.hero .line{left:450px;top:437px;width:640px;height:3px;background:var(--soft)}

.check{height:110px}
.check .bar{left:234px;top:10px;width:730px;height:74px;background:var(--soft);display:flex;align-items:center;padding:0 36px;gap:12px;color:var(--white);font-size:15px}
.check .field{width:262px;height:26px;background:var(--white);border-radius:3px}
.check .go{height:26px;padding:0 14px;border-radius:3px;background:var(--white);color:var(--deep);font-size:10px;line-height:26px;font-weight:600}
.check .note{left:0;width:1200px;top:96px;text-align:center;font-size:8.5px;color:var(--grey)}

/* welcome */
.welcome{height:410px}
.welcome h2{left:95px;top:25px;font-size:32px;font-weight:400}
.welcome h2 b{color:var(--deep);font-weight:700}
.welcome p{left:95px;top:88px;width:530px;font-size:10px;line-height:20px}
.welcome .btn{left:95px;top:182px;padding:8px 20px}
.welcome .seal{left:240px;top:180px;width:46px;height:46px;border-radius:50%;border:2px solid var(--ink)}
.welcome .tax{left:300px;top:188px;font-size:6.5px;line-height:10px;width:60px}
.welcome .doc{left:358px;top:168px;width:96px;height:132px;background:linear-gradient(#fafafa,#eceff3);border:1px solid #dcdfe4}
.welcome .docl{left:358px;top:304px;font-size:8px;color:var(--mid);text-decoration:underline}
.welcome .art{left:530px;top:10px;width:670px;height:400px;background:radial-gradient(circle at 28% 20%,var(--mid) 0,var(--mid) 10%,transparent 10.5%),radial-gradient(circle at 45% 55%,#2a8fe0 0,#2a8fe0 11%,transparent 11.5%),radial-gradient(circle at 70% 65%,#f38b3c 0,#f38b3c 11%,transparent 11.5%),linear-gradient(150deg,var(--white) 25%,var(--mist) 60%,var(--pale));border-radius:60% 0 0 0}

/* why */
.why{height:406px}
.why .art{left:90px;top:30px;width:365px;height:380px;border-radius:48% 52% 45% 55%;background:radial-gradient(circle at 40% 45%,#7c56d6 0,#7c56d6 12%,transparent 12.5%),radial-gradient(circle at 60% 50%,#2cc4ad 0,#2cc4ad 12%,transparent 12.5%),radial-gradient(circle at 55% 72%,#f06e4a 0,#f06e4a 14%,transparent 14.5%),linear-gradient(var(--mist),#e3f3ee)}
.why h2{left:524px;top:88px;font-size:32px;font-weight:400}
.why h2 b{color:var(--deep);font-weight:700}
.why ul{list-style:none;left:524px;top:152px;font-size:11.5px;line-height:31px}
.why li::before{content:"★";color:var(--deep);margin-right:6px}

/* steps */
.steps{height:364px;background:linear-gradient(90deg,var(--mid),var(--deep));border-radius:0 80px 80px 0}
.steps .blob{left:-70px;top:100px;width:300px;height:300px;border-radius:50%;background:rgba(255,255,255,.08)}
.steps .blob2{left:950px;top:220px;width:90px;height:90px;border-radius:50%;background:rgba(255,255,255,.12)}
.card{width:230px;height:259px;background:var(--white);border-radius:6px;top:55px;text-align:center;padding:34px 24px 0}
.card svg{display:block;margin:0 auto 16px}
.card h3{font-size:11.5px;line-height:17px;color:var(--mid);font-weight:600;margin-bottom:14px}
.card p{font-size:9px;line-height:14px}
.c1{left:196px}.c2{left:484px}.c3{left:772px}

/* trademark */
.trade{height:514px;background:linear-gradient(var(--white),#f4f5fb)}
.trade .art{left:40px;top:32px;width:560px;height:430px;border-radius:50%;background:radial-gradient(circle at 35% 30%,#4b5aa8 0,#4b5aa8 10%,transparent 10.5%),radial-gradient(circle at 55% 55%,#4b5aa8 0,#4b5aa8 12%,transparent 12.5%),radial-gradient(circle at 40% 70%,#5d69b8 0,#5d69b8 9%,transparent 9.5%),linear-gradient(#eef0fb,#dfe3f7)}
.trade h2{left:684px;top:155px;font-size:31px;color:var(--mid);font-weight:600}
.trade h3{left:684px;top:200px;font-size:25px;line-height:38px;font-weight:500}
.trade .steps3{left:684px;top:288px;font-size:11.5px;color:var(--mid);font-weight:600}
.trade .simple{left:684px;top:318px;font-size:24px}
.dots{display:flex;gap:5px;align-items:center}
.dots i{width:5px;height:5px;border-radius:50%;background:var(--deep)}
.dots i:first-child{width:22px;border-radius:3px}
.trade .dots{left:570px;top:482px}

/* testimonials */
.tests{height:464px;background:var(--mist)}
.tests h2{left:0;width:1200px;top:68px;text-align:center;font-size:31px;font-weight:600}
.tcard{top:129px;width:340px;height:256px;background:var(--white);border-radius:6px;padding:24px 24px}
.t1{left:70px}.t2{left:429px}.t3{left:789px}
.thead{display:flex;align-items:center;gap:16px}
.avatar{width:38px;height:38px;border-radius:50%;color:var(--white);font-size:18px;display:flex;align-items:center;justify-content:center}
.stars{color:var(--star);font-size:15px;letter-spacing:2px}
.src{margin-left:auto;font-size:9px;color:var(--grey);font-weight:600}
.tcard p{margin-top:24px;font-size:11.5px;line-height:22px}
.who{margin-top:10px;font-size:10.5px;color:var(--mid);font-weight:600}
.who span{color:var(--grey);font-weight:400;margin-left:16px;font-size:9px}
.tests .dots{left:570px;top:414px}

/* news */
.news{height:538px}
.news h2{left:0;width:1200px;top:48px;text-align:center;font-size:30px;font-weight:600}
.news .date{color:var(--deep);font-weight:600}
.news .lead .date{font-size:18px}
.news .lead{left:43px;top:110px;width:335px}
.news .lead h3{font-size:34px;line-height:52px;font-weight:600;margin-top:6px}
.news .lead p{font-size:9.5px;line-height:20px;margin-top:18px}
.more{font-size:8px;color:var(--mid);text-decoration:underline}
.news .art{left:394px;top:111px;width:302px;height:386px;background:linear-gradient(135deg,#eef1f4 20%,#b9c2cc 45%,#1f86c7 50%,#b9c2cc 56%,#eef1f4 80%);box-shadow:0 4px 10px rgba(0,0,0,.08)}
.news .list{left:789px;top:108px;width:380px}
.news .item{margin-bottom:22px}
.news .item h4{font-size:18px;line-height:30px;font-weight:600}
.news .item p{font-size:9px;line-height:19px;margin:6px 0 4px}

/* contact */
.contact{height:517px;background:var(--deep)}
.contact .art{left:0;top:60px;width:546px;height:457px;background:radial-gradient(circle at 50% 60%,#e23a6b 0,#e23a6b 22%,transparent 22.5%),radial-gradient(circle at 75% 85%,#cdb6f0 0,#cdb6f0 14%,transparent 14.5%),linear-gradient(160deg,#1f66b8,#2f7bc9)}
.contact .leaf{left:860px;top:30px;width:300px;height:120px;border-radius:50% 50% 0 0;background:linear-gradient(var(--pale),rgba(202,222,239,0))}
.form{left:560px;top:100px;width:544px;height:318px;background:var(--white);border-radius:16px;padding:90px 70px 0}
.row{display:flex;align-items:flex-end;gap:6px;height:42px;font-size:13.5px;font-weight:600;color:var(--deep)}
.row i{flex:1;border-bottom:1px solid #9aa3b2;margin-bottom:5px}
.form .btn{position:absolute;left:232px;top:258px;padding:7px 20px;font-size:9px}

/* partners */
.partners{height:158px}
.partner{top:50px;height:80px;display:flex;align-items:center;gap:8px;font-size:16px;font-weight:600;color:var(--ink);white-space:nowrap}
.partner i{width:12px;height:12px;border-radius:50%;background:var(--ink)}
.p1{left:180px}
.p2{left:420px}
.p3{left:620px}
.p4{left:880px}

/* footer */
.foot{height:196px;background:var(--deep);color:var(--white)}
.foot .brand{left:0;width:1200px;top:30px;justify-content:center;font-size:14px}
.foot ul{list-style:none;display:flex;gap:12px;left:0;width:1200px;justify-content:center;top:84px;font-size:9px}
.pay{left:0;width:1200px;top:112px;display:flex;gap:8px;justify-content:center}
.pay i{width:32px;height:14px;border-radius:2px;background:var(--white)}
.pay i:nth-child(2){width:58px;background:var(--pale)}
.social{left:0;width:1200px;top:142px;display:flex;gap:12px;justify-content:center}
.social i{width:18px;height:18px;border-radius:50%;background:var(--white)}
.copy{left:0;width:1200px;top:180px;text-align:center;font-size:7.5px}
</style>
</head>
<body>

<header class="topbar">
  <span class="abs service">Customer Service 24/7</span>
  <span class="abs phone">03 9000 0000</span>
  <a class="abs login">Log in ▾</a>
  <span class="abs search">Search here</span>
  <svg class="abs" width="11" height="11" viewBox="0 0 12 12" fill="none" stroke="#0677BA" stroke-width="1.6"><circle cx="5" cy="5" r="3.8"/><path d="M8 8l3 3"/></svg>
</header>

<nav class="nav">
  <a class="abs brand"><i></i>Firmly789</a>
  <ul class="abs">
    <li>REGISTER COMPANY ▾</li><li>BUSINESS NAME ▾</li><li>SET UP TRUST ▾</li><li>SET UP BUSINESS PLAN</li><li>REGISTER TRADE MARK ▾</li><li>SMSF</li><li>PROPERTY WITHHOLDING CLEARANCE CERTIFICATE</li><li>ABN REGISTRATION</li><li>LEGAL &amp; TAX CONSULTATIONS</li><li>PRICING</li><li>RESOURCES ▾</li>
  </ul>
</nav>

<section class="hero">
  <div class="abs art" role="img" aria-label="Illustration of a team assembling colourful puzzle pieces on a ladder"></div>
  <div class="abs line"></div>
  <h1 class="abs"><b>Australian</b> Online<br>Company <b>Registration</b></h1>
  <p class="abs lead">Simple, quick and trusted service in 3 easy online steps, for just <span>$556 *</span></p>
  <a class="abs btn btn1">REGISTER NOW</a>
  <h2 class="abs">Update your company changes to<br>ACRB for just $60</h2>
  <p class="abs agent">ACRB agent 50872</p>
  <a class="abs btn btn2">UPDATE COMPANY DETAILS</a>
</section>

<section class="check">
  <div class="abs bar">Check if company name is available <span class="field"></span><span class="go">⌕ Check</span></div>
  <p class="abs note">We take cybercrime and credit card fraud seriously. When you purchase a service through our site, we may collect your IP address for credit card security purposes</p>
</section>

<section class="welcome">
  <div class="abs art" role="img" aria-label="Illustration of two people carrying large blue puzzle pieces"></div>
  <h2 class="abs">Welcome to <b>Firmly789</b></h2>
  <p class="abs">We offer a fully automated, quick and cost effective company registration process. By completing an easy form, within 5 minutes you will receive full company registration documents setting up an Australian private company. We offer full customer support (telephone and email) 24 hours a day. It could not be any simpler, register your company today.</p>
  <a class="abs btn">MORE INFO</a>
  <div class="abs seal" role="img" aria-label="Registration badge"></div>
  <p class="abs tax">Tax agent<br>00000000</p>
  <div class="abs doc" role="img" aria-label="Sample constitution document preview"></div>
  <a class="abs docl">View Sample Constitution</a>
</section>

<section class="why">
  <div class="abs art" role="img" aria-label="Illustration of people building a wall of puzzle pieces with a crane"></div>
  <h2 class="abs"><b>Why</b> Use Us</h2>
  <ul class="abs">
    <li>Quick and simple registration process.</li>
    <li>Company registered in less than 5 minutes.</li>
    <li>Full documentation emailed to you so you can start trading.</li>
    <li>ACRB agent 50872.</li>
    <li>Prepared by a qualified lawyer and accountant.</li>
    <li>Full telephone and email customer support available 24 hours a day.</li>
    <li>The simplest and most cost effective company registration process available.</li>
  </ul>
</section>

<section class="steps">
  <div class="abs blob"></div><div class="abs blob2"></div>
  <div class="abs card c1">
    <svg width="64" height="62" viewBox="0 0 64 62" fill="none" stroke="#0054AA" stroke-width="2"><rect x="8" y="4" width="36" height="52" rx="2"/><path d="M16 16h20M16 24h20M16 32h14M16 40h10"/><path d="M40 44l16-26 4 3-16 26-5 2z"/></svg>
    <h3>Fill in a short<br>form</h3>
    <p>We offer a fully automated, quick and cost effective company registration process. By completing an easy form,</p>
  </div>
  <div class="abs card c2">
    <svg width="64" height="62" viewBox="0 0 64 62" fill="none" stroke="#0054AA" stroke-width="2"><rect x="14" y="4" width="32" height="44" rx="2"/><rect x="8" y="12" width="32" height="44" rx="2" fill="#fff"/><path d="M16 24h16M16 32h16M16 40h10"/><circle cx="46" cy="46" r="9" fill="#fff"/><path d="M42 46l3 3 5-6"/></svg>
    <h3>Company registered in<br>less than 5 minutes</h3>
    <p>We offer a fully automated, quick and cost effective company registration process. By completing an easy form,</p>
  </div>
  <div class="abs card c3">
    <svg width="64" height="62" viewBox="0 0 64 62" fill="none" stroke="#0054AA" stroke-width="2"><rect x="4" y="8" width="50" height="34" rx="2"/><path d="M14 36V26M22 36V20M30 36V24M38 36V16"/><path d="M20 42v8h18v-8M14 52h30"/><rect x="44" y="30" width="16" height="22" rx="2" fill="#fff"/><path d="M52 36v10"/></svg>
    <h3>Start trading using your<br>company</h3>
    <p>We offer a fully automated, quick and cost effective company registration process. By completing an easy form,</p>
  </div>
</section>

<section class="trade">
  <div class="abs art" role="img" aria-label="Illustration of people floating among large indigo puzzle pieces and leaves"></div>
  <h2 class="abs">Quick, Simple</h2>
  <h3 class="abs">International Trademark<br>application</h3>
  <p class="abs steps3">Completed in 3 easy steps.</p>
  <p class="abs simple">As simple as 1, 2, 3.</p>
  <div class="abs dots"><i></i><i></i><i></i><i></i></div>
</section>

<section class="tests">
  <h2 class="abs">Testimonials</h2>
  <article class="abs tcard t1">
    <div class="thead"><span class="avatar" style="background:#c0504d">B</span><span class="stars">★★★★</span><span class="src">Revuo</span></div>
    <p>I have used firmly789 to set up my company's and it's a simple process and it done properly no waiting and you received all your registration paper work in the mailRegards</p>
    <p class="who">Dana Ashfield<span>a year ago</span></p>
  </article>
  <article class="abs tcard t2">
    <div class="thead"><span class="avatar" style="background:#2d3e5c">B</span><span class="stars">★★★★★</span><span class="src">Revuo</span></div>
    <p>I have used firmly789 to set up my company's and it's a simple process and it done properly no waiting and you received all your registration paper work in the mailRegards</p>
    <p class="who">Dana Ashfield<span>a year ago</span></p>
  </article>
  <article class="abs tcard t3">
    <div class="thead"><span class="avatar" style="background:#4cbb7a">B</span><span class="stars">★★★</span><span class="src">Revuo</span></div>
    <p>I have used firmly789 to set up my company's and it's a simple process and it done properly no waiting and you received all your registration paper work in the mailRegards</p>
    <p class="who">Dana Ashfield<span>a year ago</span></p>
  </article>
  <div class="abs dots"><i></i><i></i><i></i><i></i></div>
</section>

<section class="news">
  <h2 class="abs">Latest News</h2>
  <article class="abs lead">
    <p class="date">2018/08/16 01:13</p>
    <h3>Be aware of Trademark scam and false billing.</h3>
    <p>We offer a fully automated, quick and cost effective company registration process. By completing an easy form, within 5 minutes you will receive full company registration documents setting up an Australian private company.</p>
    <a class="more">Read More</a>
  </article>
  <div class="abs art" role="img" aria-label="Photo of interlocking silver puzzle pieces with one blue piece"></div>
  <div class="abs list">
    <article class="item"><h4><span class="date">2018/08/16 12:53</span> - What is a business plan and why do you need it ?</h4><p>We offer a fully automated, quick and cost effective company registration process.</p><a class="more">Read More</a></article>
    <article class="item"><h4><span class="date">2018/08/16 12:53</span> - What is a business plan and why do you need it ?</h4><p>We offer a fully automated, quick and cost effective company registration process.</p><a class="more">Read More</a></article>
    <article class="item"><h4><span class="date">2018/08/16 12:53</span> - What is a business plan and why do you need it ?</h4><p>We offer a fully automated, quick and cost effective company registration process.</p><a class="more">Read More</a></article>
  </div>
</section>

<section class="contact">
  <div class="abs art" role="img" aria-label="Illustration of a support agent with headset working at a laptop"></div>
  <div class="abs leaf" role="img" aria-label="Decorative leaves"></div>
  <form class="abs form">
    <div class="row">Email<i></i></div>
    <div class="row">Subject<i></i></div>
    <div class="row">Message<i></i></div>
    <a class="btn">SUBMIT</a>
  </form>
</section>

<section class="partners" aria-label="Partners">
  <div class="abs partner p1"><i></i>Northway Traffic</div>
  <div class="abs partner p2"><i></i>Tallis Pay</div>
  <div class="abs partner p3"><i></i>Brightmoor Lending</div>
  <div class="abs partner p4"><i></i>Harbourstay</div>
</section>

<footer class="foot">
  <a class="abs brand"><i></i>Firmly789</a>
  <ul class="abs"><li>SET UP BUSINESS PLAN</li><li>SMSF</li><li>PROPERTY WITHHOLDING CLEARANCE CERTIFICATE</li><li>ABN REGISTRATION</li></ul>
  <div class="abs pay" aria-label="Accepted payment methods"><i></i><i></i><i></i><i></i><i></i></div>
  <div class="abs social" aria-label="Social links"><i></i><i></i><i></i><i></i></div>
  <p class="abs copy">© Firmly789 Pty Ltd 2022</p>
</footer>

</body>
</html>
```